Brantley Water Taxi and Transport

Need to redesign our business cards to relay that we do freight logistics and water taxi service. We also work with gov. agencies doing environmental clean up, oil spill response, remote site construction and work with many of the air taxi and helicopter services on Kodiak Island. Out website is www.brantleywatertaxi-example.com to get a better idea of what we do.

Contact Information for Business Card

I have a previous business card but it just has the logo on the front, and a sunset picture on the back with the contact info. It does not relay what we do and what we can help with. I like a simple straight forward design over a busy one.

Colors
3176b5
0455a3
cfdfed

Requirements
Must have
• logo, email, website, phone number

```html
<!DOCTYPE html>
<html lang="en">
<head>
<meta charset="utf-8">
<title>Brantley Water Taxi &amp; Transport – Business Card</title>
<link rel="stylesheet" href="https://fonts.googleapis.com/css2?family=Jost:wght@400;500;600&display=swap">
<style>
  :root {
    --page-bg: #e9e9e9;
    --card-white: #fafafa;
    --navy: #0455a3;
    --deep-blue: #134a8e;
    --sky: #2ea8e0;
    --ink: #2a2a2a;
    --paper-white: #ffffff;
    --mist: #cfdfed;
  }
  * { margin: 0; padding: 0; box-sizing: border-box; }
  html, body {
    width: 1200px; height: 800px; overflow: hidden;
    background: var(--page-bg);
    font-family: "Jost", "Futura", sans-serif;
  }
  .canvas { position: relative; width: 1200px; height: 800px; }

  .card {
    position: absolute; top: 278px;
    width: 420px; height: 240px;
  }
  .card--front { left: 142px; background: var(--card-white); }
  .card--back  { left: 637px; background: var(--deep-blue); }

  /* Front: name and services */
  .front-mark {
    position: absolute; left: 0; right: 0; top: 62px;
    display: flex; flex-direction: column; align-items: center;
    text-align: center;
  }
  .front-mark__main {
    color: var(--navy); font-weight: 600;
    font-size: 44px; line-height: 1; letter-spacing: 1px;
    text-transform: uppercase;
  }
  .front-mark__sub {
    margin-top: 6px;
    color: var(--ink); font-weight: 400;
    font-size: 18px; line-height: 1.1; letter-spacing: 0.3px;
  }
  .front-services {
    margin-top: 18px;
    color: var(--navy); font-weight: 500;
    font-size: 10.5px; letter-spacing: 1.2px; text-transform: uppercase;
  }
  .front-services__sep { color: var(--sky); margin: 0 5px; }

  /* Back: name and contacts */
  .back-mark {
    position: absolute; left: 101px; top: 50px;
  }
  .back-mark__main {
    display: block; color: var(--sky); font-weight: 600;
    font-size: 44px; line-height: 1; letter-spacing: 1px;
    text-transform: uppercase;
  }
  .back-mark__sub {
    display: block; margin-top: 4px;
    color: var(--paper-white); font-weight: 400;
    font-size: 19px; line-height: 1.1; letter-spacing: 0.3px;
  }

  .contact-list {
    position: absolute; left: 101px; top: 133px;
    list-style: none;
  }
  .contact-list__item {
    display: flex; align-items: center;
    height: 20.5px;
    color: var(--paper-white);
    font-size: 15px; font-weight: 400;
  }
  .contact-list__icon { width: 13px; height: 13px; margin-right: 17px; flex: none; }
</style>
</head>
<body>
<main class="canvas">

  <section class="card card--front" aria-label="Card front">
    <div class="front-mark">
      <p class="front-mark__main">Brantley</p>
      <p class="front-mark__sub">Water Taxi &amp; Transport</p>
      <p class="front-services">Freight<span class="front-services__sep">•</span>Spill Response<span class="front-services__sep">•</span>Remote Sites</p>
    </div>
  </section>

  <section class="card card--back" aria-label="Card back">
    <p class="back-mark">
      <span class="back-mark__main">Brantley</span>
      <span class="back-mark__sub">Water Taxi &amp; Transport</span>
    </p>
    <ul class="contact-list">
      <li class="contact-list__item">
        <svg class="contact-list__icon" viewBox="0 0 12 12" aria-hidden="true">
          <circle cx="6" cy="6" r="6" fill="var(--sky)"/>
          <path d="M3.6 3.2 L4.8 3 L5.4 4.5 L4.7 5.1 Q5.3 6.5 6.8 7.3 L7.4 6.6 L8.9 7.2 L8.7 8.4 Q5.2 8.6 3.6 3.2Z" fill="var(--deep-blue)"/>
        </svg>
        907 555 0148
      </li>
      <li class="contact-list__item">
        <svg class="contact-list__icon" viewBox="0 0 12 12" aria-hidden="true">
          <rect x="0.5" y="2.5" width="11" height="7.5" fill="var(--sky)"/>
          <path d="M0.5 2.5 L6 7 L11.5 2.5" fill="none" stroke="var(--deep-blue)" stroke-width="1"/>
        </svg>
        hello@brantleywatertaxi-example.com
      </li>
      <li class="contact-list__item">
        <svg class="contact-list__icon" viewBox="0 0 12 12" aria-hidden="true">
          <circle cx="6" cy="6" r="6" fill="var(--sky)"/>
          <g fill="none" stroke="var(--deep-blue)" stroke-width="0.8">
            <ellipse cx="6" cy="6" rx="2.4" ry="5.6"/>
            <line x1="0.5" y1="6" x2="11.5" y2="6"/>
            <line x1="6" y1="0.5" x2="6" y2="11.5"/>
          </g>
        </svg>
        www.brantleywatertaxi-example.com
      </li>
    </ul>
  </section>

</main>
</body>
</html>
```